Comparative Infographic

Prepare a comparison infographic for each of our (5) flavors of Coffee, the comparison is to compare the specific attributes of our products against other brands. please review our packaging and website to establish a feel for our branding. attached is the data and concept format, the format is just for informational purposes, developer should apply their own creative approach

```html
<!DOCTYPE html>
<html lang="en">
<head>
<meta charset="utf-8">
<title>Rise &amp; Ember vs Others — Flavor Comparison Boards</title>
<link rel="stylesheet" href="https://fonts.googleapis.com/css2?family=Anton&family=Poppins:wght@500;600;700&display=swap">
<style>
  :root {
    --sheet-light: #b4b4b4;
    --sheet-dark: #8c8c8c;
    --board-top: #2f7d7a;
    --board-mid: #225a5b;
    --board-bottom: #232628;
    --teal: #3a9a96;
    --teal-soft: #47a6a0;
    --mint: #8fd6a8;
    --ink: #1e1e1e;
    --row-a: #f3f3f3;
    --row-b: #ffffff;
    --rule: #cfcfcf;
    --cross: #e3262b;
    --white: #ffffff;
  }
  * { box-sizing: border-box; margin: 0; padding: 0; }
  html, body { width: 1143px; height: 1200px; overflow: hidden; }
  body {
    position: relative;
    background: radial-gradient(ellipse at 45% 40%, var(--sheet-light), var(--sheet-dark));
    font-family: "Poppins", sans-serif;
  }
  .board {
    position: absolute;
    width: 496px; height: 351px;
    overflow: hidden;
    background: linear-gradient(180deg, var(--board-top) 0%, var(--board-mid) 45%, var(--board-bottom) 100%);
    box-shadow: 0 6px 14px rgba(0,0,0,.35);
  }
  .botanical {
    position: absolute; left: 0; top: 0; width: 62px; height: 100%;
    background: linear-gradient(90deg, rgba(90,190,180,.45), rgba(60,150,145,.15) 70%, transparent);
  }
  .header-pill {
    position: absolute; left: 250px; top: 11px; width: 234px; height: 84px;
    border-radius: 14px;
    background: linear-gradient(90deg, var(--teal-soft), var(--teal));
  }
  .board--wide .header-pill { height: 93px; }
  .brand {
    position: absolute; left: 42px; top: 28px;
    display: flex; align-items: center; gap: 8px;
  }
  .brand-ring {
    width: 52px; height: 52px; border-radius: 50%;
    border: 2px solid var(--white);
  }
  .brand-name {
    font-family: "Anton", sans-serif; color: var(--white);
    font-size: 25px; line-height: .98; text-transform: uppercase; letter-spacing: .5px;
  }
  .vs {
    position: absolute; left: 218px; top: 25px; width: 64px; height: 64px;
    border-radius: 50%; background: var(--ink);
    border: 3px solid var(--mint);
    color: var(--white); font-weight: 700; font-size: 28px;
    display: flex; align-items: center; justify-content: center; line-height: 1;
  }
  .board--wide .vs { top: 30px; }
  .board--wide .brand { top: 34px; }
  .others {
    position: absolute; left: 288px; top: 18px;
    font-family: "Anton", sans-serif; color: var(--white);
    font-size: 56px; line-height: 1; letter-spacing: .5px;
  }
  .board--wide .others { top: 24px; }
  .flavor {
    position: absolute; left: 65px; top: 91px;
    font-family: "Anton", sans-serif; font-weight: 400;
    color: var(--white); font-size: 19px; line-height: 1;
    letter-spacing: -0.2px; white-space: nowrap;
  }
  .flavor span { color: var(--mint); }
  .board--wide .flavor { left: 40px; top: 116px; font-size: 26px; letter-spacing: 0; }
  .compare {
    position: absolute; left: 65px; top: 105px; width: 366px;
    border-collapse: collapse; table-layout: fixed;
  }
  .compare col.label-col { width: 154px; }
  .compare th {
    background: var(--teal); color: var(--white);
    font-size: 9.5px; font-weight: 700; height: 18px; letter-spacing: .3px;
  }
  .compare th.blank { background: transparent; }
  .compare td {
    height: 17.6px; border: 1px solid var(--rule);
    font-size: 8.2px; font-weight: 600; color: var(--ink);
    text-align: center; vertical-align: middle;
  }
  .compare tr:nth-child(odd) td { background: var(--row-a); }
  .compare tr:nth-child(even) td { background: var(--row-b); }
  .compare td.label { text-align: left; padding-left: 18px; }
  .compare td.num { color: var(--teal); font-weight: 700; font-size: 10px; }
  .compare td.tick { color: var(--teal); }
  .compare td.cross { color: var(--cross); }
  .compare svg { width: 11px; height: 11px; display: block; margin: 0 auto; }
  .board--wide .compare { left: 40px; top: 125px; width: 417px; }
  .board--wide .compare col.label-col { width: 159px; }
  .board--wide .compare th { height: 29px; font-size: 10.5px; }
  .board--wide .compare td { height: 28.6px; font-size: 9.5px; }
  .board--wide .compare td.label { padding-left: 16px; }
  .board--wide .compare svg { width: 14px; height: 14px; }
  .footnote {
    position: absolute; left: 65px; top: 315px; width: 431px; height: 22px;
    background: var(--teal); color: var(--white);
    font-size: 9.4px; font-weight: 600;
    display: flex; align-items: center; justify-content: center;
  }
</style>
</head>
<body>

<svg width="0" height="0" style="position:absolute" aria-hidden="true">
  <symbol id="tick" viewBox="0 0 16 16"><path d="M2 8.5l4 4 8-9" fill="none" stroke="currentColor" stroke-width="2.4" stroke-linecap="round" stroke-linejoin="round"/></symbol>
  <symbol id="cross" viewBox="0 0 16 16"><path d="M3 3l10 10M13 3L3 13" fill="none" stroke="currentColor" stroke-width="2.6" stroke-linecap="round"/></symbol>
</svg>

<!-- Classic Black -->
<section class="board board--wide" style="left:67px;top:57px">
  <div class="botanical" role="img" aria-label="Line-drawn coffee leaves and beans pattern"></div>
  <div class="header-pill"></div>
  <div class="brand"><span class="brand-ring"></span><span class="brand-name">Rise &amp;<br>Ember</span></div>
  <div class="vs">vs</div>
  <div class="others">Others</div>
  <h2 class="flavor">Classic Black</h2>
  <table class="compare">
    <colgroup><col class="label-col"><col><col><col><col></colgroup>
    <tr><th class="blank"></th><th>VALUE!</th><th>VALUE!</th><th>VALUE!</th><th>VALUE!</th></tr>
    <tr><td class="label">Hemp Derived THC/CBD</td><td class="tick"><svg><use href="#tick"/></svg></td><td class="cross"><svg><use href="#cross"/></svg></td><td class="cross"><svg><use href="#cross"/></svg></td><td class="cross"><svg><use href="#cross"/></svg></td></tr>
    <tr><td class="label">Nootropics</td><td class="tick"><svg><use href="#tick"/></svg></td><td class="cross"><svg><use href="#cross"/></svg></td><td class="cross"><svg><use href="#cross"/></svg></td><td class="cross"><svg><use href="#cross"/></svg></td></tr>
    <tr><td class="label">Adaptogens</td><td class="tick"><svg><use href="#tick"/></svg></td><td class="cross"><svg><use href="#cross"/></svg></td><td class="cross"><svg><use href="#cross"/></svg></td><td class="cross"><svg><use href="#cross"/></svg></td></tr>
    <tr><td class="label">Energy Booster</td><td class="tick"><svg><use href="#tick"/></svg></td><td class="cross"><svg><use href="#cross"/></svg></td><td class="cross"><svg><use href="#cross"/></svg></td><td class="cross"><svg><use href="#cross"/></svg></td></tr>
    <tr><td class="label">Healthy Fats</td><td class="tick"><svg><use href="#tick"/></svg></td><td class="cross"><svg><use href="#cross"/></svg></td><td class="cross"><svg><use href="#cross"/></svg></td><td class="cross"><svg><use href="#cross"/></svg></td></tr>
  </table>
</section>

<!-- Vanilla Latte -->
<section class="board" style="left:581px;top:57px">
  <div class="botanical" role="img" aria-label="Line-drawn coffee leaves and beans pattern"></div>
  <div class="header-pill"></div>
  <div class="brand"><span class="brand-ring"></span><span class="brand-name">Rise &amp;<br>Ember</span></div>
  <div class="vs">vs</div>
  <div class="others">Others</div>
  <h2 class="flavor">Vanilla <span>Latte</span></h2>
  <table class="compare">
    <colgroup><col class="label-col"><col><col><col></colgroup>
    <tr><th class="blank"></th><th>VALUE!</th><th>VALUE!</th><th>VALUE!</th></tr>
    <tr><td class="label">Hemp Derived THC/CBD</td><td class="tick"><svg><use href="#tick"/></svg></td><td class="cross"><svg><use href="#cross"/></svg></td><td class="cross"><svg><use href="#cross"/></svg></td></tr>
    <tr><td class="label">Nootropics</td><td class="tick"><svg><use href="#tick"/></svg></td><td class="cross"><svg><use href="#cross"/></svg></td><td class="cross"><svg><use href="#cross"/></svg></td></tr>
    <tr><td class="label">Adaptogens</td><td class="tick"><svg><use href="#tick"/></svg></td><td class="cross"><svg><use href="#cross"/></svg></td><td class="cross"><svg><use href="#cross"/></svg></td></tr>
    <tr><td class="label">Protein</td><td class="num">15</td><td class="cross"><svg><use href="#cross"/></svg></td><td class="num">7</td></tr>
    <tr><td class="label">Energy Booster</td><td class="tick"><svg><use href="#tick"/></svg></td><td class="cross"><svg><use href="#cross"/></svg></td><td class="cross"><svg><use href="#cross"/></svg></td></tr>
    <tr><td class="label">Vitamins B6 &amp; B12</td><td class="tick"><svg><use href="#tick"/></svg></td><td class="cross"><svg><use href="#cross"/></svg></td><td class="cross"><svg><use href="#cross"/></svg></td></tr>
    <tr><td class="label">Electrolytes</td><td class="tick"><svg><use href="#tick"/></svg></td><td class="cross"><svg><use href="#cross"/></svg></td><td class="cross"><svg><use href="#cross"/></svg></td></tr>
    <tr><td class="label">Healthy Fats</td><td class="tick"><svg><use href="#tick"/></svg></td><td class="cross"><svg><use href="#cross"/></svg></td><td class="cross"><svg><use href="#cross"/></svg></td></tr>
    <tr><td class="label">Added Sugar</td><td class="num">0g</td><td class="num">25g</td><td class="num">14g</td></tr>
    <tr><td class="label">Calories</td><td class="num">110*</td><td class="num">320</td><td class="num">170</td></tr>
  </table>
  <p class="footnote">* 85 calories derived from Healthy Fats (MCT) and Collagen Protein.</p>
</section>

<!-- Keto-Cream & Sugar -->
<section class="board" style="left:67px;top:425px">
  <div class="botanical" role="img" aria-label="Line-drawn coffee leaves and beans pattern"></div>
  <div class="header-pill"></div>
  <div class="brand"><span class="brand-ring"></span><span class="brand-name">Rise &amp;<br>Ember</span></div>
  <div class="vs">vs</div>
  <div class="others">Others</div>
  <h2 class="flavor">Keto-Cream <span>&amp; Sugar</span></h2>
  <table class="compare">
    <colgroup><col class="label-col"><col><col><col></colgroup>
    <tr><th class="blank"></th><th>VALUE!</th><th>VALUE!</th><th>VALUE!</th></tr>
    <tr><td class="label">Hemp Derived THC/CBD</td><td class="tick"><svg><use href="#tick"/></svg></td><td class="cross"><svg><use href="#cross"/></svg></td><td class="cross"><svg><use href="#cross"/></svg></td></tr>
    <tr><td class="label">Nootropics</td><td class="tick"><svg><use href="#tick"/></svg></td><td class="cross"><svg><use href="#cross"/></svg></td><td class="cross"><svg><use href="#cross"/></svg></td></tr>
    <tr><td class="label">Adaptogens</td><td class="tick"><svg><use href="#tick"/></svg></td><td class="cross"><svg><use href="#cross"/></svg></td><td class="cross"><svg><use href="#cross"/></svg></td></tr>
    <tr><td class="label">Protein</td><td class="num">15</td><td class="cross"><svg><use href="#cross"/></svg></td><td class="num">7</td></tr>
    <tr><td class="label">Energy Booster</td><td class="tick"><svg><use href="#tick"/></svg></td><td class="cross"><svg><use href="#cross"/></svg></td><td class="cross"><svg><use href="#cross"/></svg></td></tr>
    <tr><td class="label">Vitamins B6 &amp; B12</td><td class="tick"><svg><use href="#tick"/></svg></td><td class="cross"><svg><use href="#cross"/></svg></td><td class="cross"><svg><use href="#cross"/></svg></td></tr>
    <tr><td class="label">Electrolytes</td><td class="tick"><svg><use href="#tick"/></svg></td><td class="cross"><svg><use href="#cross"/></svg></td><td class="cross"><svg><use href="#cross"/></svg></td></tr>
    <tr><td class="label">Healthy Fats</td><td class="tick"><svg><use href="#tick"/></svg></td><td class="cross"><svg><use href="#cross"/></svg></td><td class="cross"><svg><use href="#cross"/></svg></td></tr>
    <tr><td class="label">Added Sugar</td><td class="num">4g</td><td class="num">25g</td><td class="num">14g</td></tr>
    <tr><td class="label">Calories</td><td class="num">120*</td><td class="num">150</td><td class="num">170</td></tr>
  </table>
  <p class="footnote">* 85 calories derived from Healthy Fats (MCT) and Collagen Protein.</p>
</section>

<!-- Salted Caramel -->
<section class="board" style="left:581px;top:424px">
  <div class="botanical" role="img" aria-label="Line-drawn coffee leaves and beans pattern"></div>
  <div class="header-pill"></div>
  <div class="brand"><span class="brand-ring"></span><span class="brand-name">Rise &amp;<br>Ember</span></div>
  <div class="vs">vs</div>
  <div class="others">Others</div>
  <h2 class="flavor">Salted <span>Caramel</span></h2>
  <table class="compare">
    <colgroup><col class="label-col"><col><col><col></colgroup>
    <tr><th class="blank"></th><th>VALUE!</th><th>VALUE!</th><th>VALUE!</th></tr>
    <tr><td class="label">Hemp Derived THC/CBD</td><td class="tick"><svg><use href="#tick"/></svg></td><td class="cross"><svg><use href="#cross"/></svg></td><td class="cross"><svg><use href="#cross"/></svg></td></tr>
    <tr><td class="label">Nootropics</td><td class="tick"><svg><use href="#tick"/></svg></td><td class="cross"><svg><use href="#cross"/></svg></td><td class="cross"><svg><use href="#cross"/></svg></td></tr>
    <tr><td class="label">Adaptogens</td><td class="tick"><svg><use href="#tick"/></svg></td><td class="cross"><svg><use href="#cross"/></svg></td><td class="cross"><svg><use href="#cross"/></svg></td></tr>
    <tr><td class="label">Protein</td><td class="num">15</td><td class="cross"><svg><use href="#cross"/></svg></td><td class="num">7</td></tr>
    <tr><td class="label">Energy Booster</td><td class="tick"><svg><use href="#tick"/></svg></td><td class="cross"><svg><use href="#cross"/></svg></td><td class="cross"><svg><use href="#cross"/></svg></td></tr>
    <tr><td class="label">Vitamins B6 &amp; B12</td><td class="tick"><svg><use href="#tick"/></svg></td><td class="cross"><svg><use href="#cross"/></svg></td><td class="cross"><svg><use href="#cross"/></svg></td></tr>
    <tr><td class="label">Electrolytes</td><td class="tick"><svg><use href="#tick"/></svg></td><td class="cross"><svg><use href="#cross"/></svg></td><td class="cross"><svg><use href="#cross"/></svg></td></tr>
    <tr><td class="label">Healthy Fats</td><td class="tick"><svg><use href="#tick"/></svg></td><td class="cross"><svg><use href="#cross"/></svg></td><td class="cross"><svg><use href="#cross"/></svg></td></tr>
    <tr><td class="label">Added Sugar</td><td class="num">0g</td><td class="num">50g</td><td class="num">14g</td></tr>
    <tr><td class="label">Calories</td><td class="num">110*</td><td class="num">480</td><td class="num">170</td></tr>
  </table>
  <p class="footnote">* 85 calories derived from Healthy Fats (MCT) and Collagen Protein.</p>
</section>

<!-- Café Mocha -->
<section class="board" style="left:324px;top:792px">
  <div class="botanical" role="img" aria-label="Line-drawn coffee leaves and beans pattern"></div>
  <div class="header-pill"></div>
  <div class="brand"><span class="brand-ring"></span><span class="brand-name">Rise &amp;<br>Ember</span></div>
  <div class="vs">vs</div>
  <div class="others">Others</div>
  <h2 class="flavor">Café <span>Mocha</span></h2>
  <table class="compare">
    <colgroup><col class="label-col"><col><col><col></colgroup>
    <tr><th class="blank"></th><th>VALUE!</th><th>VALUE!</th><th>VALUE!</th></tr>
    <tr><td class="label">Hemp Derived THC/CBD</td><td class="tick"><svg><use href="#tick"/></svg></td><td class="cross"><svg><use href="#cross"/></svg></td><td class="cross"><svg><use href="#cross"/></svg></td></tr>
    <tr><td class="label">Nootropics</td><td class="tick"><svg><use href="#tick"/></svg></td><td class="cross"><svg><use href="#cross"/></svg></td><td class="cross"><svg><use href="#cross"/></svg></td></tr>
    <tr><td class="label">Adaptogens</td><td class="tick"><svg><use href="#tick"/></svg></td><td class="cross"><svg><use href="#cross"/></svg></td><td class="cross"><svg><use href="#cross"/></svg></td></tr>
    <tr><td class="label">Protein</td><td class="num">15</td><td class="cross"><svg><use href="#cross"/></svg></td><td class="num">7</td></tr>
    <tr><td class="label">Energy Booster</td><td class="tick"><svg><use href="#tick"/></svg></td><td class="cross"><svg><use href="#cross"/></svg></td><td class="cross"><svg><use href="#cross"/></svg></td></tr>
    <tr><td class="label">Vitamins B6 &amp; B12</td><td class="tick"><svg><use href="#tick"/></svg></td><td class="cross"><svg><use href="#cross"/></svg></td><td class="cross"><svg><use href="#cross"/></svg></td></tr>
    <tr><td class="label">Electrolytes</td><td class="tick"><svg><use href="#tick"/></svg></td><td class="cross"><svg><use href="#cross"/></svg></td><td class="cross"><svg><use href="#cross"/></svg></td></tr>
    <tr><td class="label">Healthy Fats</td><td class="tick"><svg><use href="#tick"/></svg></td><td class="cross"><svg><use href="#cross"/></svg></td><td class="cross"><svg><use href="#cross"/></svg></td></tr>
    <tr><td class="label">Added Sugar</td><td class="num">0g</td><td class="num">44g</td><td class="num">14g</td></tr>
    <tr><td class="label">Calories</td><td class="num">110*</td><td class="num">440</td><td class="num">170</td></tr>
  </table>
  <p class="footnote">* 85 calories derived from Healthy Fats (MCT) and Collagen Protein.</p>
</section>

</body>
</html>
```